Criação de Capa para Facebook para Consultoria de Negócios
" Palestra, treinamentos e Consultoria em empresas para o crescimento profissional e pessoal dos funcionários "

```html
<!DOCTYPE html>
<html lang="pt-BR">
<head>
<meta charset="utf-8">
<title>Valorenz – Capa para Facebook</title>
<link rel="stylesheet" href="https://fonts.googleapis.com/css2?family=Montserrat:wght@400;500;600&display=swap">
<style>
  :root {
    --page-bg: #f1f1f1;
    --navy: #13283a;
    --navy-deep: #0e1f2e;
    --gold-light: #f3d99a;
    --gold: #c9a25a;
    --gold-dark: #8f6a2c;
    --white: #ffffff;
  }
  * { margin: 0; padding: 0; box-sizing: border-box; }
  html, body {
    width: 1200px;
    height: 1200px;
    overflow: hidden;
    background: var(--page-bg);
    font-family: "Montserrat", sans-serif;
  }
  .board { position: relative; width: 1200px; height: 1200px; }

  .profile-mark {
    position: absolute;
    left: 473px; top: 168px;
    width: 252px; height: 252px;
    background: var(--navy);
    display: flex; align-items: center; justify-content: center;
  }
  .profile-mark__name {
    color: var(--gold);
    font-weight: 500;
    font-size: 34px;
    letter-spacing: 1px;
  }

  .cover {
    position: absolute;
    left: 19px; top: 523px;
    width: 1162px; height: 432px;
    overflow: hidden;
    background: var(--navy);
  }
  .cover__art { position: absolute; inset: 0; }

  .cover__brand {
    position: absolute;
    left: 700px; width: 460px;
    top: 215px;
    text-align: center;
    color: var(--white);
  }
  .cover__name {
    font-weight: 500;
    font-size: 52px;
    letter-spacing: 1px;
    line-height: 1;
  }
  .cover__rule {
    width: 330px; height: 2px;
    margin: 14px auto 12px;
    background: var(--gold);
  }
  .cover__tagline {
    font-size: 17px;
    font-weight: 400;
    letter-spacing: 4px;
  }

  .cover__contacts {
    position: absolute;
    left: 800px; top: 375px;
    display: flex; gap: 26px;
    color: var(--white);
    font-size: 15px;
    font-weight: 600;
  }
  .contact { display: flex; align-items: center; gap: 7px; }
  .contact__dot {
    width: 20px; height: 20px;
    border: 2px solid var(--white);
    border-radius: 50%;
  }
</style>
</head>
<body>
<main class="board">
  <div class="profile-mark">
    <span class="profile-mark__name">VALORENZ</span>
  </div>

  <section class="cover">
    <svg class="cover__art" viewBox="0 0 1162 432" width="1162" height="432">
      <defs>
        <linearGradient id="photoTone" x1="0" y1="0" x2="1" y2="0">
          <stop offset="0" stop-color="#7f8a8c"/>
          <stop offset="0.45" stop-color="#9aa6ab"/>
          <stop offset="0.75" stop-color="#4a5e6e"/>
          <stop offset="1" stop-color="#13283a"/>
        </linearGradient>
        <linearGradient id="goldSweep" x1="0" y1="1" x2="1" y2="0">
          <stop offset="0" stop-color="#8f6a2c"/>
          <stop offset="0.4" stop-color="#f3d99a"/>
          <stop offset="0.7" stop-color="#c9a25a"/>
          <stop offset="1" stop-color="#f3d99a"/>
        </linearGradient>
      </defs>
      <rect x="0" y="0" width="760" height="432" fill="url(#photoTone)"
            role="img" aria-label="Fotografia de equipe em reunião de negócios em escritório"/>
      <path d="M455 432 C 520 230, 760 60, 1162 20 L 1162 0 L 1130 0 C 760 20, 500 200, 440 432 Z"
            fill="url(#goldSweep)"/>
      <path d="M480 432 C 545 250, 790 80, 1162 36 L 1162 432 Z" fill="var(--navy)"/>
      <path d="M480 432 C 545 250, 790 80, 1162 36" fill="none" stroke="var(--gold-dark)" stroke-width="2"/>
    </svg>

    <div class="cover__brand">
      <div class="cover__name">VALORENZ</div>
      <div class="cover__rule"></div>
      <div class="cover__tagline">TREINAMENTO E CONSULTORIA</div>
    </div>

    <div class="cover__contacts">
      <span class="contact"><span class="contact__dot"></span>/VALORENZ</span>
      <span class="contact"><span class="contact__dot"></span>(XX) XXXX-XXXX</span>
    </div>
  </section>
</main>
</body>
</html>
```